NDF Job bank

National Dental Fellowship Needs a design for our orthodontist job bank.

We are in the process of redesigning our current job board. We would like to improve our current design, focusing on the landing page and possibly the search page. I have attached images of what we currently have in place right now.

The Landing page: Currently, I find the landing page too wordy, members get confused when using it, we need something that is easier for providers are seekers to use. Set up more user friendly. Maybe have a button for become provider and become seeker and then a modal pops up with process.. The final design for this page needs to be user friendly, organized and clean. If someone were coming to this page for the first time they would know how to become a provider.

The search page: I was thinking it would be best to have the search options on the left hand side opposed to how it is just in the middle now. all of the information currently shown on this page needs to be included. The search results need improvement on how they are displayed as well.

If you have any questions feel free to contact me.

Industry/Entity Type

Bank

Number of Pages Required

1 page

Colors
33a6d7
85cae6
0692cd

Requirements
Must have
• A Landing page that is well designed and that is made in the blue colors that are shown on the attached files of what our job bank currently looks like. I have also attached 3 photos that could be used for a masthead, but keep in mind these do not have to be used, you can use any photo you would like, these are just for your convenience.
Nice to have
• An improved search results page along with the Landing page

```html
<!DOCTYPE html>
<html lang="en">
<head>
<meta charset="utf-8">
<title>NDF Job Bank</title>
<link rel="stylesheet" href="https://fonts.googleapis.com/css2?family=Source+Sans+3:wght@300;400;600&family=Arimo:wght@400&display=swap">
<style>
:root{
  --blue:#0692cd;
  --blue-mid:#33a6d7;
  --blue-light:#85cae6;
  --blue-bright:#12a6e4;
  --navy:#1b2f86;
  --ink:#444;
  --muted:#666;
  --footer:#222;
  --white:#fff;
}
*{box-sizing:border-box;margin:0;padding:0}
html,body{width:1200px;height:2314px;overflow:hidden;background:var(--white)}
body{position:relative;font-family:"Source Sans 3",sans-serif;color:var(--ink)}

.site-header{position:absolute;left:0;top:0;width:1200px;height:221px}
.brand{position:absolute;left:86px;top:68px;display:flex;align-items:center;gap:18px}
.brand-square{width:118px;height:116px;background:var(--blue);border-radius:8px}
.brand-name{font-size:34px;line-height:36px;font-weight:400;color:var(--navy);width:220px}
.account-links{position:absolute;right:86px;top:86px;font-size:18px;color:var(--muted);letter-spacing:.3px}
.search-box{position:absolute;left:853px;top:135px;width:261px;height:35px;border:1px solid #cfcfcf;padding:0 12px;display:flex;align-items:center;justify-content:space-between;font-size:14px;color:#999}

.main-nav{position:absolute;left:0;top:221px;width:1200px;height:59px;background:linear-gradient(#2aaee2,#0f95d0);display:flex;padding-left:88px}
.main-nav a{display:flex;align-items:center;padding:0 25px;color:var(--white);text-decoration:none;font-size:19px;text-transform:uppercase;border-right:1px solid rgba(0,0,0,.12)}
.main-nav a.active{background:var(--blue-light);background:linear-gradient(#56bfea,#3aaee0)}
.main-nav a:last-child{border-right:0}

.hero{position:absolute;left:0;top:280px;width:1200px;height:570px;background:linear-gradient(100deg,#c9dbe8 0%,#e3eef4 45%,#f4f8fb 100%)}
.hero-arrow{position:absolute;top:509px;width:60px;height:60px}
.hero-arrow.prev{left:87px}
.hero-arrow.next{left:1051px}

.welcome{position:absolute;left:95px;top:920px;width:1010px;text-align:center}
.welcome h1{font-size:36px;font-weight:400;color:#333}
.welcome h1 span{color:var(--navy)}
.welcome p{margin-top:24px;font-size:14px;line-height:26px;color:var(--muted)}

.role-card{position:absolute;top:1155px;width:444px;height:686px;border-radius:10px;background:linear-gradient(#0b90cd,#14a8e6 45%,#0b93d0);color:var(--white);text-align:center;box-shadow:0 22px 16px -14px rgba(0,0,0,.35)}
.role-card.provider{left:122px}
.role-card.seeker{left:641px}
.role-card h2{margin-top:42px;font-size:44px;font-weight:300;letter-spacing:1px}
.role-card .tagline{margin-top:14px;font-size:23px}
.role-card hr{margin:24px 36px 0;border:0;border-top:1px solid rgba(255,255,255,.35)}
.steps{list-style:none;margin-top:18px}
.steps li{font-size:23px;line-height:34px}
.steps svg{display:block;margin:6px auto 8px}
.role-btn{display:block;margin:32px auto 0;width:252px;height:50px;border:2px solid var(--white);font-size:22px;line-height:46px;text-transform:uppercase}

.newsletter{position:absolute;left:117px;top:1932px;width:970px;height:51px}
.newsletter h3{position:absolute;left:0;top:0;font-size:42px;font-weight:300;color:#555;line-height:51px}
.newsletter .email{position:absolute;left:477px;top:0;width:338px;height:51px;border:2px solid #555;padding-left:14px;font-size:14px;line-height:47px;font-family:Arimo,sans-serif;color:#333}
.newsletter .signup{position:absolute;left:815px;top:0;width:155px;height:51px;background:var(--blue);color:var(--white);font-size:24px;text-align:center;line-height:51px}

.site-footer{position:absolute;left:0;top:2055px;width:1200px;height:259px;background:var(--footer);color:var(--white);font-family:Arimo,sans-serif;text-align:center}
.social{position:absolute;left:0;top:50px;width:1200px;height:62px}
.footer-links{position:absolute;top:154px;width:1200px;font-size:14px}
.copyright{position:absolute;top:190px;width:1200px;font-size:14px}
</style>
</head>
<body>
<header class="site-header">
  <div class="brand"><div class="brand-square"></div><div class="brand-name">National Dental Fellowship</div></div>
  <div class="account-links">JOIN &nbsp;|&nbsp; SIGN IN</div>
  <div class="search-box">Search..
    <svg width="14" height="14" viewBox="0 0 14 14"><circle cx="6" cy="6" r="4.5" fill="none" stroke="#999" stroke-width="1.6"/><line x1="9.5" y1="9.5" x2="13" y2="13" stroke="#999" stroke-width="1.8"/></svg>
  </div>
</header>

<nav class="main-nav">
  <a class="active">Meetings &amp; Events</a><a>Education</a><a>Practice Management</a><a>Publications</a><a>Legal</a><a>Communities</a>
</nav>

<section class="hero" role="img" aria-label="Smiling dental team in white coats, blue tinted photo">
  <svg class="hero-arrow prev" viewBox="0 0 60 60"><circle cx="30" cy="30" r="30" fill="rgba(60,60,60,.6)"/><polyline points="34,20 24,30 34,40" fill="none" stroke="#fff" stroke-width="2"/></svg>
  <svg class="hero-arrow next" viewBox="0 0 60 60"><circle cx="30" cy="30" r="30" fill="rgba(120,120,120,.6)"/><polyline points="26,20 36,30 26,40" fill="none" stroke="#fff" stroke-width="2"/></svg>
</section>

<section class="welcome">
  <h1>Welcome To <span>Our Website</span></h1>
  <p>Typi non habent claritatem insitam; est usus legentis in iis qui facit eorum claritatem. Investigationes demonstraverunt lectores legere me lius quod ii legunt saepius. Claritas est etiam processus dynamicus, qui sequitur mutationem consuetudium lectorum. Mirum est notare quam littera gothica, quam nunc putamus parum claram, anteposuerit litterarum formas humanitatis per seacula quarta decima et quinta decima. Eodem modo typi, qui nunc nobis videntur parum clari, fiant sollemnes in futurum.</p>
</section>

<section class="role-card provider">
  <h2>PROVIDER</h2>
  <div class="tagline">Post an Oppurtunity or Search Resumes</div>
  <hr>
  <ul class="steps">
    <li>Request Access</li>
    <li><svg width="22" height="16" viewBox="0 0 22 16"><polyline points="3,2 11,8 19,2" fill="none" stroke="#fff" stroke-width="2"/><polyline points="3,8 11,14 19,8" fill="none" stroke="#fff" stroke-width="2"/></svg>Post Oppurtunity</li>
    <li><svg width="22" height="16" viewBox="0 0 22 16"><polyline points="3,2 11,8 19,2" fill="none" stroke="#fff" stroke-width="2"/><polyline points="3,8 11,14 19,8" fill="none" stroke="#fff" stroke-width="2"/></svg>Search the Resume Center</li>
    <li><svg width="22" height="16" viewBox="0 0 22 16"><polyline points="3,2 11,8 19,2" fill="none" stroke="#fff" stroke-width="2"/><polyline points="3,8 11,14 19,8" fill="none" stroke="#fff" stroke-width="2"/></svg>Access Your Oppurtunities</li>
    <li><svg width="22" height="16" viewBox="0 0 22 16"><polyline points="3,2 11,8 19,2" fill="none" stroke="#fff" stroke-width="2"/><polyline points="3,8 11,14 19,8" fill="none" stroke="#fff" stroke-width="2"/></svg>Frequently Asked Questions</li>
  </ul>
  <span class="role-btn">Become Provider</span>
</section>

<section class="role-card seeker">
  <h2>SEEKER</h2>
  <div class="tagline">Post an Oppurtunity or Search Resumes</div>
  <hr>
  <ul class="steps">
    <li>Request Access</li>
    <li><svg width="22" height="16" viewBox="0 0 22 16"><polyline points="3,2 11,8 19,2" fill="none" stroke="#fff" stroke-width="2"/><polyline points="3,8 11,14 19,8" fill="none" stroke="#fff" stroke-width="2"/></svg>Post Oppurtunity</li>
    <li><svg width="22" height="16" viewBox="0 0 22 16"><polyline points="3,2 11,8 19,2" fill="none" stroke="#fff" stroke-width="2"/><polyline points="3,8 11,14 19,8" fill="none" stroke="#fff" stroke-width="2"/></svg>Search the Resume Center</li>
    <li><svg width="22" height="16" viewBox="0 0 22 16"><polyline points="3,2 11,8 19,2" fill="none" stroke="#fff" stroke-width="2"/><polyline points="3,8 11,14 19,8" fill="none" stroke="#fff" stroke-width="2"/></svg>Access Your Oppurtunities</li>
    <li><svg width="22" height="16" viewBox="0 0 22 16"><polyline points="3,2 11,8 19,2" fill="none" stroke="#fff" stroke-width="2"/><polyline points="3,8 11,14 19,8" fill="none" stroke="#fff" stroke-width="2"/></svg>Frequently Asked Questions</li>
  </ul>
  <span class="role-btn">Become Seeker</span>
</section>

<section class="newsletter">
  <h3>Signup for Newsletter</h3>
  <div class="email">Enter the Email Id</div>
  <div class="signup">SIGNUP</div>
</section>

<footer class="site-footer">
  <svg class="social" viewBox="0 0 1200 62" aria-label="Social links">
    <circle cx="507" cy="31" r="29" fill="none" stroke="#ddd" stroke-width="2"/>
    <circle cx="585" cy="31" r="29" fill="none" stroke="#ddd" stroke-width="2"/>
    <circle cx="663" cy="31" r="29" fill="none" stroke="#ddd" stroke-width="2"/>
    <circle cx="739" cy="31" r="29" fill="none" stroke="#ddd" stroke-width="2"/>
  </svg>
  <div class="footer-links">Home &nbsp;|&nbsp; Explore &nbsp;|&nbsp; NDF Member Directory &nbsp;|&nbsp; About &nbsp;|&nbsp; Contact</div>
  <div class="copyright">Copyright © 2013. All Rights Reserved.</div>
</footer>
</body>
</html>
```